TotHaven Community Landing Page

TotHaven is a virtual world built with childrens' needs in mind. It is an online portal where parents will find all kids' related stuffs and a community connect point for parents to interact and share their experiences.

We need the designs for 2 pages within TotHaven:
- Landing Page for the Community Area
- Registration page for membership

1) The Landing Page need to have the following:

Logo & Main Background :- use the images attached

Page Title & Navigation Menu :-
The page title is "Community Connect"; navigation menu should be able to hold at least 6 tabs

Login Widget* :-
We want to put emphasis on the design of this.
For visitors, this is a normal login widget with username/password input fields, register button and 'login with chatterbook' button.
For logged-in users, this becomes a simple dashboard widget with Avatar, shortlinks and some useful navigation buttons.

"Groups" Section :-
This area holds an image, a short paragraph introducing "Groups", a widget showing 5-10 latest/popular groups and a 'Go to Groups' button at the bottom.

"Forum" Section :-
This area holds an image, a short paragraph introducing "Forum", a widget showing 5-10 latest/popular discussion topics and a 'Go to Forum' button at the bottom.

"Activities" Section -
This area holds an image, a short paragraph introducing "Forum", a widget showing 5-10 latest/popular events & activities and a 'Go to Activities' button at the bottom.

"Marketplace" Section :-
This area holds an image, a short paragraph introducing "Marketplace", a widget showing 5-10 latest/popular products and a 'Go to Marketplace' button at the bottom.

Social Media elements :-
The usual social media icons and chatterbook like box.

2) The Registration Page will need to contain the registration form as per the image attached.

Target Market(s)

Parents with kids ranging from 2 - 12 years old

Industry/Entity Type

Events

Requirements
Nice to have
• - colorful illustrations of kids or kids related images all around

```html
<!DOCTYPE html>
<html lang="en">
<head>
<meta charset="utf-8">
<title>TotHaven Community Connect</title>
<link rel="stylesheet" href="https://fonts.googleapis.com/css2?family=Ubuntu:wght@300;400;500&display=swap">
<style>
:root{
  --sky-top:#7cc6ec;
  --sky-low:#cfeefa;
  --grass:#6e9a2c;
  --grass-dark:#55801f;
  --nav:#6a4fb5;
  --nav-dark:#55399e;
  --white:#ffffff;
  --line:#e4e4e4;
  --ink:#333333;
  --muted:#8a8a8a;
  --orange:#f07f12;
  --green:#3f9a2a;
  --purple:#9a2fb0;
  --red:#d42b3a;
  --login:#f39a16;
}
*{box-sizing:border-box;margin:0;padding:0}
html,body{width:716px;height:1200px;overflow:hidden}
body{font-family:"Ubuntu",sans-serif;color:var(--ink);
  background:linear-gradient(180deg,var(--sky-top) 0,var(--sky-low) 260px,#e9f6fb 300px,#8fb94a 330px,var(--grass) 420px,var(--grass-dark) 1200px);}
.page{position:relative;width:716px;height:1200px}
.abs{position:absolute}

.brand{left:36px;top:26px;display:flex;align-items:center;gap:8px}
.brand-dot{width:36px;height:36px;border-radius:50%;background:#e53c8a}
.brand-name{font-size:30px;font-weight:500;color:#8e2fb8}

.login{left:448px;top:20px;width:228px;height:30px;border-radius:15px;background:rgba(255,255,255,.55);display:flex;align-items:center;gap:4px;padding:0 8px}
.field{height:18px;border-radius:9px;background:var(--white);font-size:7px;color:#9a9a9a;padding:0 10px;line-height:18px;width:81px}
.login-btn{height:18px;border-radius:9px;background:var(--login);color:#fff;font-size:8px;font-weight:500;line-height:18px;padding:0 10px}
.search{left:498px;top:60px;width:179px;height:22px;border-radius:11px;background:var(--white);font-size:7px;color:#9a9a9a;line-height:22px;padding-left:12px}
.search svg{position:absolute;right:8px;top:5px}

.nav{left:38px;top:94px;width:640px;height:36px;border-radius:10px 10px 0 0;background:linear-gradient(var(--nav),var(--nav-dark));display:flex;padding-left:109px}
.nav a{color:#fff;text-decoration:none;font-size:11px;line-height:36px;padding:0 13px;border-right:1px solid rgba(255,255,255,.25)}
.nav a:last-child{border-right:0}

.hero{left:38px;top:126px;width:641px;height:232px;border-radius:12px;background:var(--white);padding:4px 8px}
.hero-photo{width:626px;height:222px;border-radius:8px;background:linear-gradient(100deg,#f2c7a8,#f7e6d0 45%,#b7dcf0 80%,#f0d0e0)}
.dots{left:330px;top:334px;width:56px;height:16px;border-radius:8px 8px 0 0;background:var(--nav);display:flex;gap:3px;justify-content:center;align-items:center}
.dots i{width:5px;height:5px;border-radius:50%;background:#2a1f57}
.dots i:first-child{background:#fff}

.panel{left:38px;top:364px;width:641px;height:758px;border-radius:12px;background:var(--white)}

.card{position:absolute;width:293px;height:272px;border:1px solid var(--line);border-radius:6px;background:#fff;box-shadow:0 1px 2px rgba(0,0,0,.06)}
.card h2{position:absolute;left:16px;top:14px;font-size:18px;font-weight:400}
.card-photo{position:absolute;left:14px;top:40px;width:94px;height:79px;border-radius:4px}
.card-intro{position:absolute;left:120px;top:41px;width:160px}
.card-intro h3{font-size:9.5px;font-weight:400;color:#333;margin-bottom:2px}
.card-intro p{font-size:7.5px;line-height:14px;color:var(--muted);font-weight:300;margin-bottom:2px}
.card ul{position:absolute;left:16px;top:128px;width:258px;list-style:none}
.card li{font-size:8px;height:20px;line-height:20px;border-bottom:1px solid #efefef;padding-left:10px;position:relative}
.card li:last-child{border-bottom:0}
.card li::before{content:"";position:absolute;left:1px;top:7px;border-left:4px solid currentColor;border-top:3px solid transparent;border-bottom:3px solid transparent}
.btn{position:absolute;left:16px;top:233px;height:22px;line-height:22px;padding:0 14px;border-radius:3px;color:#fff;font-size:8px}
.groups{left:56px;top:385px}.groups h2,.groups li{color:var(--orange)}.groups .btn{background:linear-gradient(#f79a35,#e46f05)}
.forum{left:366px;top:385px}.forum h2,.forum li{color:var(--green)}.forum .btn{background:linear-gradient(#55b23a,#2f851d)}
.activities{left:57px;top:673px}.activities h2,.activities li{color:var(--purple)}.activities .btn{background:linear-gradient(#a95cc4,#7d2e9c)}
.market{left:367px;top:673px}.market h2,.market li{color:var(--red)}.market .btn{background:linear-gradient(#e2545f,#bf1f2d)}

.box{position:absolute;top:958px;width:293px;height:148px;border:1px solid var(--line);border-radius:4px;background:#fff}
.like{left:56px}
.like-logo{position:absolute;left:16px;top:16px;width:50px;height:40px;background:#f6b640}
.like-name{position:absolute;left:73px;top:17px;font-size:9.5px}
.like-btn{position:absolute;left:73px;top:33px;font-size:6.5px;color:#3b5998;border:1px solid #c7cfe0;background:#eef1f7;padding:1px 4px}
.like-count{position:absolute;left:16px;top:59px;font-size:7px}
.fans{position:absolute;left:16px;top:74px;display:flex;gap:2px}
.fans span{width:35px;height:35px}
.plugin{position:absolute;left:16px;top:120px;font-size:7px;display:flex;align-items:center;gap:3px}
.plugin i{width:10px;height:10px;background:#3b5998;display:block}
.posts{left:364px}
.posts h2{position:absolute;left:20px;top:14px;font-size:16px;font-weight:300;color:#555}
.post{position:absolute;left:20px;width:260px;font-size:7.5px;line-height:13px;color:var(--muted);font-weight:300}
.post b{display:block;color:var(--green);font-weight:500;font-size:7px}

.footer-links{left:48px;top:1140px;font-size:8px;color:#fff}
.footer-links a{color:#fff;text-decoration:none}
.copy{left:48px;top:1157px;font-size:7px;color:#e5f0d5}
.social{left:578px;top:1139px;display:flex;gap:3px}
.social span{width:22px;height:22px;border-radius:50%;background:#fff;border:2px solid #e3eccf}
</style>
</head>
<body>
<div class="page">
  <div class="abs brand"><span class="brand-dot"></span><span class="brand-name">TotHaven</span></div>

  <div class="abs login">
    <span class="field">username</span><span class="field">password</span><span class="login-btn">Login</span>
  </div>
  <div class="abs search">type word here
    <svg width="11" height="11" viewBox="0 0 11 11"><circle cx="4.5" cy="4.5" r="3.5" fill="none" stroke="#888" stroke-width="1.2"/><line x1="7" y1="7" x2="10" y2="10" stroke="#888" stroke-width="1.4"/></svg>
  </div>

  <nav class="abs nav">
    <a href="#">HOME</a><a href="#">GROUPS</a><a href="#">FORUMS</a><a href="#">ACTIVITIES</a><a href="#">MARKETPLACE</a><a href="#">CONTACT US</a>
  </nav>

  <div class="abs hero"><div class="hero-photo" role="img" aria-label="Three smiling children in colourful party costumes"></div></div>
  <div class="abs dots"><i></i><i></i><i></i><i></i></div>

  <div class="abs panel"></div>

  <section class="card groups">
    <h2>Our Groups</h2>
    <div class="card-photo" role="img" aria-label="Children laughing together" style="background:linear-gradient(135deg,#f3d2bd,#a9cde8)"></div>
    <div class="card-intro"><h3>Duis tincidunt lectus quis viverra</h3><p>Suspendisse vulputate aliquam dui. Nulla elementum dui ut augue.</p><p>Aliquam vehicula mi at mauris. Maecenas placerat, nisl at consequat rhoncus</p></div>
    <ul><li>Duis tincidunt lectus quis dui viverra</li><li>Vivamus porttitor g purus nisi eleifend libero</li><li>Etiam est nunc venenatis in tristique eu imperdiet ac nisl</li><li>Suspendisse quam leo molestie sed luctus quis feugiat in</li><li>Vivamus porttitor g urus nisi eleifend</li></ul>
    <a class="btn">Go to Forum</a>
  </section>

  <section class="card forum">
    <h2>Forum</h2>
    <div class="card-photo" role="img" aria-label="Child smelling a sunflower" style="background:linear-gradient(135deg,#8fb45a,#e9c24a)"></div>
    <div class="card-intro"><h3>Duis tincidunt lectus quis viverra</h3><p>Suspendisse vulputate aliquam dui. Nulla elementum dui ut augue.</p><p>Aliquam vehicula mi at mauris. Maecenas placerat, nisl at consequat</p></div>
    <ul><li>Duis tincidunt lectus quis dui viverra</li><li>Vivamus porttitor g purus nisi eleifend libero</li><li>Etiam est nunc venenatis in tristique eu imperdiet ac nisl</li><li>Suspendisse quam leo molestie sed luctus quis feugiat in</li><li>Vivamus porttitor g urus nisi eleifend</li></ul>
    <a class="btn">Go to Groups</a>
  </section>

  <section class="card activities">
    <h2>Activities</h2>
    <div class="card-photo" role="img" aria-label="Colourful birthday cake" style="background:linear-gradient(135deg,#f1d6a0,#f5ecd8)"></div>
    <div class="card-intro"><h3>Duis tincidunt lectus quis viverra</h3><p>Suspendisse vulputate aliquam dui. Nulla elementum dui ut augue.</p><p>Aliquam vehicula mi at mauris. Maecenas placerat, nisl at consequat rhoncus</p></div>
    <ul><li>Duis tincidunt lectus quis dui viverra</li><li>Vivamus porttitor g purus nisi eleifend libero</li><li>Etiam est nunc venenatis in tristique eu imperdiet ac nisl</li><li>Suspendisse quam leo molestie sed luctus quis feugiat in</li><li>Vivamus porttitor g urus nisi eleifend</li></ul>
    <a class="btn">Go to Activities</a>
  </section>

  <section class="card market">
    <h2>Marketplace</h2>
    <div class="card-photo" role="img" aria-label="Ferris wheel against a blue sky" style="background:linear-gradient(135deg,#3d7fd0,#9cc7ef)"></div>
    <div class="card-intro"><h3>Duis tincidunt lectus quis viverra</h3><p>Suspendisse vulputate aliquam dui. Nulla elementum dui ut augue.</p><p>Aliquam vehicula mi at mauris. Maecenas placerat, nisl at consequat</p></div>
    <ul><li>Duis tincidunt lectus quis dui viverra</li><li>Vivamus porttitor g purus nisi eleifend libero</li><li>Etiam est nunc venenatis in tristique eu imperdiet ac nisl</li><li>Suspendisse quam leo molestie sed luctus quis feugiat in</li><li>Vivamus porttitor g urus nisi eleifend</li></ul>
    <a class="btn">Go to Marketplace</a>
  </section>

  <section class="box like">
    <div class="like-logo"></div>
    <div class="like-name">TotHaven</div>
    <div class="like-btn">Like</div>
    <div class="like-count">220 people like TotHaven</div>
    <div class="fans" role="img" aria-label="Profile photos of fans">
      <span style="background:#8aa6bf"></span><span style="background:#6a86b0"></span><span style="background:#d8b9a4"></span><span style="background:#7a5a48"></span><span style="background:#b08a78"></span><span style="background:#777"></span><span style="background:#3a3040"></span>
    </div>
    <div class="plugin"><i></i>chatterbook social plugin</div>
  </section>

  <section class="box posts">
    <h2>Latest Posts</h2>
    <div class="post" style="top:40px">Phasellus felis dolor, scelerisque a, tempus eget, lobortis id, libero. Donec scelerisque leo ac risus. Praesent sit amet est.<b>Posted 2 hours ago</b></div>
    <div class="post" style="top:84px">In dictum, dolor eu dictum porttitor, enim felis viverra mi, eget luctus massa purus quis odio. Etiam nulla massa<b>Posted 5 hours ago</b></div>
  </section>

  <div class="abs footer-links"><a href="#">HOME</a> &nbsp;|&nbsp; <a href="#">GROUPS</a> &nbsp;|&nbsp; <a href="#">FORUMS</a> &nbsp;|&nbsp; <a href="#">ACTIVITIES</a> &nbsp;|&nbsp; <a href="#">MARKETPLACE</a> &nbsp;|&nbsp; <a href="#">CONTACT US</a></div>
  <div class="abs copy">© 2013 Company Name. All right reserved. Term of Use</div>
  <div class="abs social"><span></span><span></span><span></span><span></span></div>
</div>
</body>
</html>
```